Business Card for Industrial Distributor

We need a business card design for an industrial distributor. We sell machine parts for the manufacturing and oil industry. We would like the cards to look clean and modern but with a touch of industry.

Our colors are blue/white.

Please feel free to visit our website www.krovelmint.com

Target Market(s)

mexican manufacturers in the automobile/aerospace industry

Industry/Entity Type

Industrial

Colors
ffffff
0555a3

```html
<!DOCTYPE html>
<html lang="en">
<head>
<meta charset="utf-8">
<title>Krovelmint Business Card</title>
<link href="https://fonts.googleapis.com/css2?family=Roboto:wght@300;700&display=swap" rel="stylesheet">
<style>
  :root {
    --page: #ffffff;
    --card: #ffffff;
    --card-edge: #6d6e71;
    --band: #77787b;
    --band-text: #ffffff;
    --brand: #373f95;
    --brand-mark: #0555a3;
    --contact: #6d6e71;
  }
  html, body {
    margin: 0;
    padding: 0;
    width: 1200px;
    height: 761px;
    overflow: hidden;
    background: var(--page);
    font-family: "Roboto", Arial, sans-serif;
  }
  .canvas {
    position: relative;
    width: 1200px;
    height: 761px;
  }
  .card {
    position: absolute;
    top: 207px;
    width: 458px;
    height: 296px;
    background: var(--card);
    border: 1px solid var(--card-edge);
    overflow: hidden;
  }
  .card--front { left: 116px; }
  .card--back { left: 590px; }

  .web-band {
    position: absolute;
    width: 262px;
    height: 40px;
  }
  .web-band svg {
    position: absolute;
    inset: 0;
  }
  .web-band__text {
    position: absolute;
    top: 0;
    line-height: 40px;
    font-weight: 300;
    font-size: 18px;
    color: var(--band-text);
    white-space: nowrap;
  }
  .card--front .web-band { top: 0; left: 0; }
  .card--front .web-band__text { left: 31px; }
  .card--back .web-band { bottom: 0; right: 0; width: 250px; }
  .card--back .web-band__text { right: 20px; }

  .brand {
    position: absolute;
    top: 116px;
    left: 68px;
    display: flex;
    align-items: center;
    gap: 12px;
  }
  .brand__dot {
    width: 60px;
    height: 60px;
    border-radius: 50%;
    background: var(--brand-mark);
  }
  .brand__name {
    font-weight: 700;
    font-size: 48px;
    letter-spacing: 0.5px;
    color: var(--brand);
    line-height: 1;
  }

  .contact {
    position: absolute;
    left: 25px;
    top: 236px;
    font-weight: 300;
    font-size: 13px;
    line-height: 21px;
    color: var(--contact);
    white-space: nowrap;
  }
  .contact__phone { word-spacing: 6px; }
</style>
</head>
<body>
<main class="canvas">
  <section class="card card--front">
    <div class="web-band">
      <svg width="262" height="40" viewBox="0 0 262 40" aria-hidden="true">
        <polygon points="0,0 262,0 234,40 0,40" fill="var(--band)"/>
      </svg>
      <span class="web-band__text">www.krovelmint.com</span>
    </div>
    <div class="brand">
      <span class="brand__dot"></span>
      <span class="brand__name">Krovelmint</span>
    </div>
    <div class="contact">
      <div class="contact__phone">+524 81 555 0147</div>
      <div class="contact__email">krovelmint@vantrelsys.net</div>
    </div>
  </section>

  <section class="card card--back">
    <div class="web-band">
      <svg width="250" height="40" viewBox="0 0 250 40" aria-hidden="true">
        <polygon points="28,0 250,0 250,40 0,40" fill="var(--band)"/>
      </svg>
      <span class="web-band__text">www.krovelmint.com</span>
    </div>
    <div class="brand">
      <span class="brand__dot"></span>
      <span class="brand__name">Krovelmint</span>
    </div>
  </section>
</main>
</body>
</html>
```